サイト構成・基本的な要件については
https://zuvela.com/boards/7kQwLmTn28XpaRzd
をご参照ください。
ただ、レイアウトについては、各コンテンツへの導線が確保されていれば、
上記レイアウト案を必ず守る必要はございません。

写真素材については、
http://hakoyuki.jp/fetch/8b1d2f7a4c6e90135d7a8b2c4e6f1a3b5d7c9e0a
よりダウンロードください。
また、こちらだけですと作成が難しいと思いますので。。
http://gorumo.jp/
などから、10000円程度までならこちらにて購入可能です。

ロゴについては、
添付のデータを展開していただく形でご利用ください。

丸太のマークをご利用いただければ、
その他の要素(Wood Working Shop / 浅沼工房の丸太文字)については
必ずしも使用しなくてかまいません。
位置の変更も問題ございません。

【参考サイト】
http://www.surinavel.com/
http://kabuteya.jp/

白ベースの配色で、
少し木の温かみを感じるようなデザインを希望いたします。

基本レイアウト
については、必ずしも忠実である必要はありません。
特に今後大きく構成が変わる予定はございませんので、
各コンテンツへの導線を確保してあれば
必ずしも上記に準じている必要はありません。
ご自由にご提案いただいても結構です。
2カラムのご提案でも問題ございません。
また、当方jqueryを使用したコーディングも可能です。

恐れ入りますが、何卒よろしくお願いいたします。
http://www.lumio-t.hinoka.ne.jp/
茶系
【素材データについて】
よりダウンロードください。
http://gorumo.jp/
カンプデータにて作成頂き、納品時に当方にて購入したデータに差し替えていただければと存じます。

【参考サイト】
http://www.surinavel.com/
http://kabuteya.jp/

落ち着きがあり、信頼性を感じるデザインを希望いたします。
トップページで、いくつかの施工写真を見せられればと思います。
あまり無機質になりすぎず、木の温かみを感じるようなイメージですと
大変ありがたく存じます。

http://pagebase-lab.com/2012/166.html
http://pagebase-lab.com/2011/115.html
→フッター部分の参考です

ご提案に関しまして、不明点等ございましたらお気軽にお申し付けください。

クライアントとの協議の結果、こちらの案を採用させていただきました。
サイト全体の見やすさ、信頼感、清潔感
文字などの読みやすさが大変気に入り、
そちらが採用の決め手となりました。

この度は多数ご提案いただきありがとうございました。
当選に至らなかったランサー様におかれましては大変心苦しいのですが、
次の機会にぜひご提案いただければ幸甚です。
引き続き何卒よろしくお願いいたします。

```html
<!DOCTYPE html>
<html lang="ja">
<head>
<meta charset="utf-8">
<title>株式会社 浅沼工房</title>
<link rel="stylesheet" href="https://fonts.googleapis.com/css2?family=Noto+Sans+JP:wght@400;500;700&family=Noto+Serif+JP:wght@500;700&display=swap">
<style>
:root{
  --bg:#ffffff;
  --text:#4a3f36;
  --muted:#8a8078;
  --line:#ddd6cc;
  --wood:#c89a63;
  --wood-light:#e3c59c;
  --wood-dark:#8b6440;
  --green:#7fae4e;
  --nav-bg:#f7f4ef;
  --footer:#efece7;
}
*{margin:0;padding:0;box-sizing:border-box}
html,body{width:877px;height:1200px;overflow:hidden;background:var(--bg)}
body{font-family:"Noto Sans JP",sans-serif;color:var(--text);font-size:11px;position:relative}
.wrap{position:absolute;left:130px;width:616px}

/* header */
.site-header{top:22px;height:50px}
.brand{position:absolute;left:0;top:6px;display:flex;align-items:center;gap:8px}
.brand-mark{width:26px;height:26px;border-radius:50%;background:var(--text)}
.brand-sub{font-size:7px;letter-spacing:2px;color:var(--muted);display:block}
.brand-name{font-size:17px;font-weight:700;color:var(--text);letter-spacing:1px}
.header-contact{position:absolute;right:0;top:4px;display:flex;gap:10px;align-items:flex-end}
.header-contact .addr{font-size:7px;color:var(--muted);text-align:right;line-height:1.6}
.header-contact .tel{font-size:13px;color:var(--text);display:block}
.btn-mail{background:var(--green);color:#fff;font-size:8px;padding:7px 12px;display:flex;align-items:center;gap:5px;border-radius:2px}

/* nav */
.global-nav{top:82px;height:36px;display:flex;border:1px solid var(--line);background:var(--nav-bg)}
.global-nav a{flex:1;display:flex;align-items:center;justify-content:center;font-size:10px;color:var(--text);text-decoration:none;border-right:1px solid var(--line)}
.global-nav a:last-child{border-right:none}
.global-nav a.current{background:#fff}

/* hero */
.hero{top:124px;height:308px;display:grid;grid-template-columns:232px 192px 192px;grid-template-rows:154px 154px;gap:0}
.hero-lead{background:linear-gradient(180deg,#d8b07c,#b98550);display:flex;align-items:center;justify-content:center}
.hero-lead p{width:150px;height:150px;border-radius:50%;background:rgba(255,255,255,.85);display:flex;flex-direction:column;align-items:center;justify-content:center;font-family:"Noto Serif JP",serif;color:var(--wood-dark);font-weight:700;font-size:14px;line-height:1.7;text-align:center}
.hero-lead small{font-size:8px;color:var(--muted);font-weight:500}
.photo{display:block}
.hero-bottom{grid-column:1/4;display:grid;grid-template-columns:repeat(4,1fr)}

/* news */
.news{top:470px;width:372px}
.section-title{font-family:"Noto Serif JP",serif;font-size:15px;font-weight:500;border-bottom:1px solid var(--line);padding-bottom:6px;display:flex;justify-content:space-between;align-items:flex-end}
.section-title span{font-size:7px;color:var(--muted);font-family:"Noto Sans JP",sans-serif}
.news-list{list-style:none}
.news-list li{display:flex;gap:12px;font-size:8px;padding:13px 0;border-bottom:1px dotted var(--line);color:var(--text)}
.news-list time{color:var(--muted)}

.contact-box{top:470px;left:522px;width:224px;height:160px;border:1px solid var(--wood);background:#fff}
.contact-box h2{background:var(--wood);color:#fff;font-size:10px;font-weight:500;padding:6px 10px}
.contact-box .tel-line{display:flex;align-items:center;gap:6px;padding:5px 12px 0;font-size:17px;color:var(--text)}
.contact-box .tel-line b{font-size:9px;font-weight:500;color:var(--wood-dark);width:26px}
.contact-box .hours{font-size:7px;color:var(--muted);padding:4px 12px}
.contact-box .btn-mail{margin:6px 12px;justify-content:center}

/* gallery */
.works{top:686px;height:307px;display:grid;grid-template-columns:repeat(5,1fr);grid-template-rows:repeat(3,1fr);gap:4px}

/* footer */
.site-footer{position:absolute;left:0;top:1013px;width:877px;height:187px;background:var(--footer);border-top:1px solid var(--line)}
.footer-nav{display:flex;flex-wrap:wrap;justify-content:center;gap:4px 16px;width:360px;margin:22px auto 0;font-size:8px;color:var(--muted)}
.footer-brand{display:flex;align-items:center;justify-content:center;gap:8px;margin-top:22px}
.footer-brand .brand-mark{width:22px;height:22px}
.footer-brand .brand-name{font-size:15px}
.copyright{text-align:center;font-size:7px;color:var(--muted);margin-top:22px}
</style>
</head>
<body>

<header class="wrap site-header">
  <div class="brand">
    <span class="brand-mark"></span>
    <div><span class="brand-sub">WOOD WORKING SHOP</span><span class="brand-name">株式会社 浅沼工房</span></div>
  </div>
  <div class="header-contact">
    <div class="addr">神奈川県架空市見本町1-2-3<span class="tel">Tel : 0465-00-4821</span></div>
    <a class="btn-mail"><svg width="10" height="8" viewBox="0 0 10 8"><rect x=".5" y=".5" width="9" height="7" fill="none" stroke="#fff"/><path d="M.5 .5 5 4.5 9.5 .5" fill="none" stroke="#fff"/></svg>メールでお問い合わせ</a>
  </div>
</header>

<nav class="wrap global-nav">
  <a class="current">トップページ</a><a>事業内容</a><a>施工例</a><a>お取引の流れ</a><a>よくあるご質問</a><a>会社概要</a>
</nav>

<section class="wrap hero">
  <div class="hero-lead"><p><small>創業以来の確かな技術</small>木製建具・家具のことなら<br>お任せください!</p></div>
  <div class="photo" role="img" aria-label="和室の施工写真" style="background:linear-gradient(160deg,#efe6d6,#cdb48f)"></div>
  <div class="photo" role="img" aria-label="窓際の木製建具の施工写真" style="background:linear-gradient(160deg,#e9ecea,#a9b59c)"></div>
  <div class="hero-bottom">
    <div class="photo" role="img" aria-label="障子のある和室の写真" style="background:linear-gradient(180deg,#f3efe6,#c9b28b)"></div>
    <div class="photo" role="img" aria-label="木製の引き戸の写真" style="background:linear-gradient(180deg,#dcc6a4,#9b7550)"></div>
    <div class="photo" role="img" aria-label="格子戸のある廊下の写真" style="background:linear-gradient(180deg,#e4d5bd,#a98560)"></div>
    <div class="photo" role="img" aria-label="木製家具のある室内の写真" style="background:linear-gradient(180deg,#f1ede6,#cfc3b0)"></div>
  </div>
</section>

<section class="wrap news">
  <h2 class="section-title">新着情報<span>一覧を見る</span></h2>
  <ul class="news-list">
    <li><time>2017.01.20</time>ここに新着情報のテキストが入ります。施工例を更新しました。</li>
    <li><time>2017.01.12</time>ここに新着情報のテキストが入ります。年始の営業日のお知らせ。</li>
    <li><time>2016.12.25</time>ここに新着情報のテキストが入ります。年末の営業日のお知らせ。</li>
    <li><time>2016.12.01</time>ここに新着情報のテキストが入ります。ホームページを公開しました。</li>
  </ul>
</section>

<aside class="wrap contact-box">
  <h2>お見積り・ご相談はこちら</h2>
  <p class="tel-line"><b>TEL</b>0465-00-4821</p>
  <p class="tel-line"><b>FAX</b>0465-00-4822</p>
  <p class="hours">受付時間 8:00〜17:00（日祝休み）</p>
  <a class="btn-mail"><svg width="10" height="8" viewBox="0 0 10 8"><rect x=".5" y=".5" width="9" height="7" fill="none" stroke="#fff"/><path d="M.5 .5 5 4.5 9.5 .5" fill="none" stroke="#fff"/></svg>メールでお問い合わせ</a>
</aside>

<section class="wrap works" aria-label="施工例">
  <div role="img" aria-label="施工例：木製の棚" style="background:linear-gradient(#e6d2b4,#b58c5f)"></div>
  <div role="img" aria-label="施工例：和室の建具" style="background:linear-gradient(#efe7d9,#c7ae88)"></div>
  <div role="img" aria-label="施工例：格子の建具" style="background:linear-gradient(#d9c19c,#9a7249)"></div>
  <div role="img" aria-label="施工例：収納家具" style="background:linear-gradient(#eee7dc,#d0bb98)"></div>
  <div role="img" aria-label="施工例：木製の下駄箱" style="background:linear-gradient(#f0e6d4,#c19e72)"></div>
  <div role="img" aria-label="施工例：室内の引き戸" style="background:linear-gradient(#efe9df,#c4b193)"></div>
  <div role="img" aria-label="施工例：木製カウンター" style="background:linear-gradient(#dcb98c,#8e6540)"></div>
  <div role="img" aria-label="施工例：白い室内" style="background:linear-gradient(#f4f2ee,#d6d0c6)"></div>
  <div role="img" aria-label="施工例：木製の扉" style="background:linear-gradient(#e1c8a3,#a57c52)"></div>
  <div role="img" aria-label="施工例：棚の並ぶ部屋" style="background:linear-gradient(#ece3d3,#bfa27b)"></div>
  <div role="img" aria-label="施工例：廊下の建具" style="background:linear-gradient(#efe8dc,#c8b291)"></div>
  <div role="img" aria-label="施工例：ロッカー家具" style="background:linear-gradient(#e9dcc6,#b8966b)"></div>
  <div role="img" aria-label="施工例：障子" style="background:linear-gradient(#f3efe7,#d2c2a6)"></div>
  <div role="img" aria-label="施工例：造作家具" style="background:linear-gradient(#d6b68d,#946b45)"></div>
  <div role="img" aria-label="施工例：白い収納" style="background:linear-gradient(#f3f0ea,#d4cabb)"></div>
</section>

<footer class="site-footer">
  <nav class="footer-nav">
    <span>トップページ</span><span>事業内容</span><span>施工例</span><span>お取引の流れ</span><span>よくあるご質問</span>
    <span>会社概要</span><span>プライバシーポリシー</span><span>サイトマップ</span><span>お問い合わせ</span>
  </nav>
  <div class="footer-brand">
    <span class="brand-mark"></span>
    <span class="brand-name">株式会社 浅沼工房</span>
  </div>
  <p class="copyright">Copyright © 2017 株式会社浅沼工房 All Rights Reserved.</p>
</footer>

</body>
</html>
```